Mobile Oil Change company needs a flyer to promote new business

We need a flyer to 1) print & handout and 2) email out to potential customers. We are a mobile oil change company that comes to our customer locations to perform the work instead of customers going to traditional oil change companies. We have a 21 point inspection with our oil change. (21 point inspection details will not be on the flyer). Would like to keep the flyer simple but creative. I'm attaching 1) the write-up we created, 2) our logo (logo color is dark teal on white but other combinations are included if you wanted to propose a different color combination), and 3) additional services we offer. Logo font is Alegreya Sans.
Would like the additional services listed with icons and brief descriptions (similar to attachment) without pricing. Company website for reference is www.brindlefleetcare.com.

Target Market(s)

Companies with many service vehicles such as Oil & Gas service companies, heating and air conditioning companies, utility companies, police departments, etc. Companies that prioritize convenience and maintenance first.

Font styles to use
Sans Serif

Colors
00a990

Requirements
Must have
• Simple but creative design with our logo at top of the flyer. Additional Services (details in document supplied) can be smaller and less prominent than other "main" content listed in the CONTENT document supplied.
Should not have
• Do not use animated character graphics in the flyer and limit (1) stock photos to A small area in the flyer.

```html
<!DOCTYPE html>
<html lang="en">
<head>
<meta charset="utf-8">
<title>Brindle Fleet Care – Flyer</title>
<link href="https://fonts.googleapis.com/css2?family=Source+Sans+3:wght@400;600;700&display=swap" rel="stylesheet">
<style>
  :root{
    --stage:#3d3d3d;
    --teal-dark:#165955;
    --teal-mid:#0e7a6e;
    --teal-bright:#00a990;
    --ink:#1c1c1c;
    --paper:#ffffff;
  }
  *{box-sizing:border-box;margin:0;padding:0}
  html,body{width:1200px;height:1200px;overflow:hidden;background:var(--stage);font-family:"Source Sans 3",sans-serif}
  .flyer{position:absolute;left:202px;top:42px;width:794px;height:1114px;background:var(--paper);overflow:hidden;box-shadow:0 6px 20px rgba(0,0,0,.45)}
  .header{position:absolute;left:0;top:0;width:794px;height:350px}
  .brand{position:absolute;left:0;right:0;top:68px;text-align:center;color:var(--paper);font-weight:700;line-height:1}
  .brand-name{font-size:84px;letter-spacing:2px;display:block}
  .brand-sub{font-size:26px;letter-spacing:6px;display:block;margin-top:10px}
  .headline{position:absolute;left:0;right:0;text-align:center;color:var(--paper);font-weight:700;line-height:1}
  .headline.big{top:204px;font-size:62px;letter-spacing:-1px}
  .headline.sub{top:260px;font-size:50px;letter-spacing:-1px}
  .intro{position:absolute;left:50px;top:362px;width:720px;font-size:24px;line-height:31px;color:var(--ink)}
  .steps{position:absolute;left:44px;top:0;width:740px;list-style:none}
  .step{position:absolute;left:0;display:flex;align-items:center;gap:6px;white-space:nowrap;font-size:23.5px;color:var(--ink)}
  .step-icon{width:42px;height:42px;background:var(--teal-dark);display:flex;align-items:center;justify-content:center;flex:none}
  .step-icon svg{width:28px;height:28px}
  .rule{position:absolute;left:0;width:794px;height:3px;background:var(--teal-bright)}
  .section-pill{position:absolute;left:224px;top:738px;width:318px;height:47px;border-radius:24px;background:var(--teal-dark);color:var(--paper);font-size:31px;font-weight:600;text-align:center;line-height:46px}
  .service{position:absolute;width:240px;text-align:center;color:var(--ink)}
  .service svg{display:block;margin:0 auto;width:40px;height:40px}
  .service h3{font-size:13.5px;font-weight:700;color:var(--teal-dark);margin-top:8px}
  .service p{font-size:10.5px;line-height:14px;margin-top:8px}
  .footer{position:absolute;left:0;bottom:0;width:794px;height:64px;background:var(--teal-dark);color:var(--paper);display:flex;align-items:center;justify-content:center;gap:22px;font-size:14.5px}
  .footer .sep{opacity:.9}
  .footer span{display:flex;align-items:center;gap:10px}
  .footer svg{width:15px;height:15px}
</style>
</head>
<body>
<div class="flyer">
  <svg class="header" viewBox="0 0 794 350" preserveAspectRatio="none" aria-hidden="true">
    <defs>
      <radialGradient id="headGlow" cx="0.5" cy="0.35" r="0.6">
        <stop offset="0" stop-color="#06a68e"/>
        <stop offset="0.55" stop-color="#0f7a6f"/>
        <stop offset="1" stop-color="#175855"/>
      </radialGradient>
    </defs>
    <path d="M0 0H794V307Q560 352 400 347Q200 342 0 322Z" fill="url(#headGlow)"/>
  </svg>

  <div class="brand">
    <span class="brand-name">BRINDLE</span>
    <span class="brand-sub">FLEET CARE</span>
  </div>
  <div class="headline big">HASSLE FREE</div>
  <div class="headline sub">OIL CHANGES ON YOUR TERMS</div>

  <p class="intro">Our simple 5-step process lets you schedule an appointment and save time &amp; money</p>

  <ul class="steps">
    <li class="step" style="top:439px">
      <span class="step-icon"><svg viewBox="0 0 28 28" fill="none" stroke="#fff" stroke-width="1.6"><rect x="3" y="9" width="22" height="15"/><path d="M3 9l11-6 11 6M3 24l9-8M25 24l-9-8M3 9l11 9 11-9"/></svg></span>
      Call or email us to schedule service
    </li>
    <li class="step" style="top:495px">
      <span class="step-icon"><svg viewBox="0 0 28 28" fill="#fff"><circle cx="14" cy="8" r="5"/><path d="M4 26c0-7 4-11 10-11s10 4 10 11z"/></svg></span>
      Our highly trained technicians come to you for service
    </li>
    <li class="step" style="top:559px">
      <span class="step-icon"><svg viewBox="0 0 28 28" fill="none" stroke="#fff" stroke-width="1.5"><path d="M8 8h11v11H8M19 12h4l3 4v3h-7"/><circle cx="11" cy="20" r="2"/><circle cx="22" cy="20" r="2"/><path d="M2 11h5M3 14h4M1 17h6"/></svg></span>
      Service is performed quickly on your vehicle
    </li>
    <li class="step" style="top:621px">
      <span class="step-icon"><svg viewBox="0 0 28 28" fill="none" stroke="#fff" stroke-width="1.5"><path d="M6 3h11l5 5v17H6z"/><path d="M10 14h8M10 17h8M10 20h8"/></svg></span>
      Pay agreed-upon pricing and receipt is emailed to you
    </li>
    <li class="step" style="top:678px">
      <span class="step-icon"><svg viewBox="0 0 28 28" fill="none" stroke="#fff" stroke-width="2.2"><circle cx="14" cy="14" r="8"/><circle cx="14" cy="14" r="2.5" fill="#fff"/><path d="M14 1v5M14 22v5M1 14h5M22 14h5"/></svg></span>
      Services performed are tracked electronically &amp; reminders created
    </li>
  </ul>

  <div class="rule" style="top:757px"></div>
  <div class="rule" style="top:767px"></div>
  <div class="section-pill">Additional Services</div>

  <div class="service" style="left:22px;top:800px">
    <svg viewBox="0 0 40 40" fill="none" stroke="#00a990" stroke-width="1.4"><rect x="3" y="2" width="34" height="36"/><path d="M8 6v28M14 6v28M20 6v28M26 6v28M32 6v28M4 10h32M4 30h32"/></svg>
    <h3>Engine Air Filter Replacement</h3>
    <p>Maintain optimum engine performance.<br>Recommended every 15,000 - 30,000<br>miles.</p>
  </div>
  <div class="service" style="left:283px;top:796px">
    <svg viewBox="0 0 40 40" fill="none" stroke="#00a990" stroke-width="1.4"><path d="M8 2h24v36H8z"/><path d="M2 14c6-4 12 4 18 0s12 4 18 0M2 21c6-4 12 4 18 0s12 4 18 0M2 28c6-4 12 4 18 0s12 4 18 0"/></svg>
    <h3>Cabin Air Filter Replacement</h3>
    <p>Maintain a clean A/C and fan system.<br>Recommended every 12months or<br>15,000 - 25,000</p>
  </div>
  <div class="service" style="left:538px;top:800px">
    <svg viewBox="0 0 40 40" fill="none" stroke="#00a990" stroke-width="1.4"><path d="M3 14q17-10 34 0L21 34Q20 36 19 34z"/><path d="M20 30l-9-14M5 4l1 1M20 0v2M35 4l-1 1" stroke-dasharray="2 2"/></svg>
    <h3 style="margin-top:4px">Wiperblade Replacement</h3>
    <p>Maintain excellent visibility on the road.<br>Recommended by 6-12 months.</p>
  </div>

  <div class="service" style="left:22px;top:928px">
    <svg viewBox="0 0 40 40" fill="none" stroke="#00a990" stroke-width="1.6"><circle cx="20" cy="20" r="18"/><circle cx="20" cy="20" r="13"/><circle cx="20" cy="20" r="3"/><path d="M7 18h10M23 18h10M20 23v10"/></svg>
    <h3>Power Steering Fliud Flush</h3>
    <p style="margin-top:6px">Maintain proper power steering system health.<br>Recommnended every 30,000 - 60,000 miles.</p>
  </div>
  <div class="service" style="left:283px;top:928px">
    <svg viewBox="0 0 40 40" fill="none" stroke="#00a990" stroke-width="1.6"><path d="M6 4h18v34H6zM3 38h24"/><rect x="10" y="8" width="10" height="8"/><path d="M24 10l6 5v14a3 3 0 0 0 6 0V16l-4-5"/></svg>
    <h3>Fuel System Treatment</h3>
    <p style="margin-top:6px">Clean your fuel system and injectors<br>to improve fuel economy.</p>
  </div>
  <div class="service" style="left:538px;top:928px">
    <svg viewBox="0 0 40 40" fill="none" stroke="#00a990" stroke-width="1.4"><circle cx="20" cy="20" r="17"/><circle cx="20" cy="20" r="9"/><circle cx="20" cy="20" r="3"/><path d="M27 4q10 5 10 16" stroke-width="4"/></svg>
    <h3>Brake Fluid Flush</h3>
    <p style="margin-top:6px">Maintain an excellent functioning brake<br>system. Recommended every 2years or<br>20,000 miles.</p>
  </div>

  <footer class="footer">
    <span>Call&nbsp; - (833) 555-0148</span>
    <span class="sep">|</span>
    <span><svg viewBox="0 0 16 16" fill="#fff"><path d="M0 3h16v10H0z"/><path d="M0 3l8 6 8-6" stroke="#165955" stroke-width="1.3" fill="none"/></svg>sales@brindlefleetcare.com</span>
    <span class="sep">|</span>
    <span><svg viewBox="0 0 16 16" fill="none" stroke="#fff" stroke-width="1.2"><circle cx="8" cy="8" r="7"/><ellipse cx="8" cy="8" rx="3" ry="7"/><path d="M1 8h14M2.5 4.5h11M2.5 11.5h11"/></svg>www.brindlefleetcare.com</span>
  </footer>
</div>
</body>
</html>
```